Bitcoin Casino User Interface

This is a responsive design for a new bitcoin casino called the brass lantern casino

The 4 games I need the Ui for are video poker, blackjack, roulette and dice

The designs should be ideal for mobile and have a bit of a retro feel

Good example is www.pixelroulettehallcom

Target Market(s)

Adults between the ages of 21-55 all over the world

Industry/Entity Type

Casino

Font styles to use
Serif

Colors
5dc4b5
ffffff

Requirements
Must have
• Must be responsive and look great on mobile
design must be functional
Should not have
• Any generic and standard elements

```html
<!DOCTYPE html>
<html lang="en">
<head>
<meta charset="utf-8">
<title>The Brass Lantern Casino – Video Poker</title>
<link rel="stylesheet" href="https://fonts.googleapis.com/css2?family=Oswald:wght@400;500&family=Roboto+Condensed:wght@400;700&family=Libre+Baskerville:wght@400;700&display=swap">
<style>
:root{
  --navy:#0b2440;
  --navy-deep:#071a30;
  --panel:#12345a;
  --teal:#5dc4b5;
  --teal-bright:#38c6e0;
  --teal-mid:#1d8fb0;
  --teal-dark:#0f5f82;
  --gold:#f2c230;
  --white:#ffffff;
  --ink:#111111;
  --red:#e0201c;
  --line:rgba(255,255,255,.55);
}
*{box-sizing:border-box;margin:0;padding:0}
html,body{width:1200px;height:800px;overflow:hidden;background:var(--navy-deep)}
.screen{
  position:relative;width:1200px;height:800px;overflow:hidden;
  background:radial-gradient(ellipse at 50% 52%,var(--teal-bright) 0%,var(--teal-mid) 35%,var(--teal-dark) 62%,var(--navy) 100%);
  font-family:"Roboto Condensed",sans-serif;color:var(--white);
}
.top-rule,.bottom-rule{position:absolute;left:40px;right:40px;height:2px;background:var(--gold)}
.top-rule{top:52px}.bottom-rule{bottom:40px}
.brand{position:absolute;top:14px;left:0;right:0;display:flex;justify-content:center;align-items:center;gap:10px;
  font-family:"Oswald",sans-serif;font-size:22px;letter-spacing:1px;text-transform:uppercase;color:var(--white)}
.brand-dot{width:18px;height:18px;border-radius:50%;background:var(--white)}

/* pay table */
.paytable{position:absolute;left:380px;top:72px;width:440px;border:1px solid var(--line);border-collapse:collapse;font-size:13px;line-height:1}
.paytable td{padding:2px 6px;text-align:center;border-left:1px solid var(--line)}
.paytable td.hand{text-align:left;border-left:none;width:130px}
.paytable td.on{background:rgba(7,26,48,.55)}
.paytable tr.win td{background:var(--gold);color:var(--navy)}

/* games menu */
.games{position:absolute;left:40px;top:230px;width:210px}
.games-tab{width:120px;height:34px;background:var(--teal-bright);font-family:"Oswald",sans-serif;font-size:18px;display:flex;align-items:center;justify-content:center}
.game{height:88px;background:var(--navy);border-bottom:2px solid var(--panel);display:flex;flex-direction:column;align-items:center;justify-content:center;gap:6px;
  font-family:"Oswald",sans-serif;font-size:22px}
.game.active{color:var(--gold)}
.game svg{width:26px;height:26px}

/* chat */
.chat{position:absolute;right:40px;top:82px;width:200px;height:340px;background:var(--navy);font-size:11px;line-height:1.35}
.chat-tab{position:absolute;top:-16px;left:0;width:100%;height:30px;background:var(--teal-bright);font-family:"Oswald",sans-serif;font-size:18px;display:flex;align-items:center;justify-content:center}
.chat-log{list-style:none;padding:26px 12px 0}
.chat-log li{margin-bottom:8px}
.chat-log li::before{content:"• ";color:var(--teal)}
.chat-input{position:absolute;left:12px;right:12px;bottom:14px;height:30px;background:var(--white);color:#555;font-size:11px;padding:6px}

/* cards */
.hand-row{position:absolute;left:310px;top:290px;width:560px;height:210px}
.card{position:absolute;top:40px;width:104px;height:150px;background:var(--white);border-radius:7px;color:var(--ink);
  font-family:"Libre Baskerville",serif;box-shadow:0 6px 14px rgba(0,0,0,.3)}
.card.red{color:var(--red)}
.card.held{outline:3px solid var(--gold)}
.card .rank{position:absolute;top:6px;left:7px;font-size:16px;line-height:1;text-align:center}
.card .rank.rev{top:auto;left:auto;bottom:6px;right:7px;transform:rotate(180deg)}
.card .pips{position:absolute;inset:26px 22px;display:grid;grid-template-columns:1fr 1fr;align-content:space-between;font-size:20px;text-align:center;line-height:1}
.card .ace{position:absolute;inset:0;display:flex;align-items:center;justify-content:center;font-size:56px}
.card .face-art{position:absolute;inset:26px 20px;background:linear-gradient(160deg,#3c5fa8,#d9b23a 55%,#c23030);border:1px solid var(--ink)}
.hold{position:absolute;top:12px;font-family:"Oswald",sans-serif;font-size:15px}

/* controls */
.credits{position:absolute;left:806px;top:574px;font-family:"Oswald",sans-serif;font-size:17px}
.bet{position:absolute;left:540px;top:580px;font-family:"Oswald",sans-serif;font-size:17px}
.btn{position:absolute;top:608px;height:26px;padding:0 10px;background:var(--navy);display:flex;align-items:center;justify-content:center;font-size:14px;white-space:nowrap}
.tab{position:absolute;top:720px;height:26px;background:var(--teal-bright);display:flex;align-items:center;justify-content:center;font-size:14px;padding:0 12px}
.tab.current{background:var(--gold);color:var(--navy)}
.recent-list{position:absolute;left:520px;top:646px;width:90px;height:74px;background:var(--navy);list-style:none;padding:5px 8px;font-size:12px;line-height:1.3}
.recent-list li:first-child{color:var(--gold)}
.chip{position:absolute;width:22px;height:22px;border-radius:50%;background:var(--gold);border:3px dashed var(--navy)}
</style>
</head>
<body>
<main class="screen">
  <header class="brand"><span class="brand-dot"></span>The Brass Lantern Casino</header>
  <div class="top-rule"></div>

  <table class="paytable">
    <tr><td class="hand">Royal Flush</td><td>250</td><td>500</td><td class="on">750</td><td>1000</td><td>4000</td></tr>
    <tr><td class="hand">Straight Flush</td><td>50</td><td>100</td><td class="on">150</td><td>200</td><td>250</td></tr>
    <tr><td class="hand">Four of a Kind</td><td>25</td><td>50</td><td class="on">75</td><td>100</td><td>125</td></tr>
    <tr><td class="hand">Full House</td><td>9</td><td>18</td><td class="on">27</td><td>36</td><td>45</td></tr>
    <tr><td class="hand">Flush</td><td>6</td><td>12</td><td class="on">18</td><td>24</td><td>30</td></tr>
    <tr class="win"><td class="hand">Straight</td><td>4</td><td>8</td><td>12</td><td>16</td><td>20</td></tr>
    <tr><td class="hand">Three of a Kind</td><td>3</td><td>6</td><td class="on">9</td><td>12</td><td>15</td></tr>
    <tr><td class="hand">Two Pair</td><td>2</td><td>4</td><td class="on">6</td><td>8</td><td>10</td></tr>
    <tr><td class="hand">Jacks or Better</td><td>1</td><td>2</td><td class="on">3</td><td>4</td><td>5</td></tr>
  </table>

  <nav class="games">
    <div class="games-tab">GAMES</div>
    <div class="game active"><svg viewBox="0 0 26 26"><circle cx="13" cy="13" r="12" fill="#f2c230"/><circle cx="13" cy="13" r="6" fill="#0b2440"/></svg>Video Poker</div>
    <div class="game"><svg viewBox="0 0 26 26"><rect x="5" y="2" width="16" height="22" rx="2" fill="#fff"/><text x="13" y="17" font-size="9" text-anchor="middle" fill="#111" font-family="Roboto Condensed, sans-serif">21</text></svg>Blackjack</div>
    <div class="game"><svg viewBox="0 0 26 26"><circle cx="13" cy="13" r="11" fill="none" stroke="#fff" stroke-width="2"/><circle cx="13" cy="13" r="6" fill="none" stroke="#fff" stroke-width="2"/><circle cx="13" cy="13" r="2" fill="#fff"/></svg>Roulette</div>
    <div class="game"><svg viewBox="0 0 26 26"><rect x="2" y="8" width="13" height="13" rx="2" fill="#fff"/><rect x="11" y="3" width="13" height="13" rx="2" fill="#fff" stroke="#0b2440"/><circle cx="6" cy="12" r="1.3" fill="#0b2440"/><circle cx="11" cy="17" r="1.3" fill="#0b2440"/><circle cx="17.5" cy="9.5" r="1.5" fill="#0b2440"/></svg>Dice</div>
  </nav>
  <span class="chip" style="left:236px;top:404px"></span>

  <aside class="chat">
    <div class="chat-tab">CHAT</div>
    <ul class="chat-log">
      <li>Welcome to Brass Lantern Video Poker (03/03/2014 3:00pm)</li>
      <li>4a7f21c9d0 has left (03/03/2014 3:02pm)</li>
      <li>4a7f21c9d0 has joined</li>
      <li>8b2e90f1a3 has left</li>
      <li>8b2e90f1a3 has joined</li>
      <li>News: We have added 2 factor authentication and…</li>
    </ul>
    <div class="chat-input">Your message…</div>
  </aside>
  <span class="chip" style="left:946px;top:282px"></span>

  <section class="hand-row">
    <div class="hold" style="left:150px">Hold</div>
    <div class="hold" style="left:264px">Hold</div>
    <div class="card red" style="left:0"><div class="rank">5<br>♦</div><div class="pips"><span>♦</span><span>♦</span><span style="grid-column:1/3">♦</span><span>♦</span><span>♦</span></div><div class="rank rev">5<br>♦</div></div>
    <div class="card held" style="left:114px"><div class="rank">A<br>♠</div><div class="ace">♠</div><div class="rank rev">A<br>♠</div></div>
    <div class="card red held" style="left:228px"><div class="rank">K<br>♥</div><div class="face-art" role="img" aria-label="King of hearts court card artwork"></div><div class="rank rev">K<br>♥</div></div>
    <div class="card red" style="left:342px"><div class="rank">9<br>♥</div><div class="pips"><span>♥</span><span>♥</span><span>♥</span><span>♥</span><span style="grid-column:1/3">♥</span><span>♥</span><span>♥</span><span>♥</span><span>♥</span></div><div class="rank rev">9<br>♥</div></div>
    <div class="card" style="left:456px"><div class="rank">10<br>♣</div><div class="pips"><span>♣</span><span>♣</span><span>♣</span><span>♣</span><span>♣</span><span>♣</span><span>♣</span><span>♣</span><span>♣</span><span>♣</span></div><div class="rank rev">10<br>♣</div></div>
  </section>

  <div class="bet">BET: 3</div>
  <div class="credits">CREDITS: 50</div>
  <div class="btn" style="left:600px;width:100px">Cash/Credit</div>
  <div class="btn" style="left:706px;width:80px">Bet</div>
  <div class="btn" style="left:792px;width:100px">Bet Max</div>
  <div class="btn" style="left:898px;width:100px">Draw/Deal</div>

  <ul class="recent-list"><li>Video Poker</li><li>Blackjack</li><li>Roulette</li><li>Dice</li></ul>
  <div class="tab current" style="left:520px;width:90px">Recent</div>
  <div class="tab" style="left:616px;width:96px">My Games</div>
  <div class="tab" style="left:718px;width:90px">Big Wins</div>
  <div class="tab" style="left:814px;width:90px">Rare Wins</div>
  <div class="tab" style="left:910px;width:110px">Leaderboard</div>
  <div class="tab" style="left:1026px;width:90px">Account</div>
  <span class="chip" style="left:736px;top:690px"></span>
  <div class="bottom-rule"></div>
</main>
</body>
</html>
```